Wedding Invitation and envelope package

I need the 1st of many invitation designs. This is a floral collection and I have attached many designs that I like from competitors. I think that the pastel look is the best but I am hoping you can make something special. The font selection is just as important as the imagery. The overall size with bleeds is 5.25 x 7.25" and I have attached a sample to make sure sizing is clear. I also need A7 envelopes to go with the invitation, front and back flap. I want someone to look at the design and say they would pick it over any of the samples. I will need 8 total floral designs done over the next few weeks after this 1st one is done. I will also need a collection of 8 modern designs done. Please ask any questions

Font styles to use
Serif
Sans Serif
Script

Requirements
Must have
• This is a single sided invitation, a back side is not needed.
Should not have
• No full solid dark backgrounds

```html
<!DOCTYPE html>
<html lang="en">
<head>
<meta charset="utf-8">
<title>A7 Envelope – Floral Collection</title>
<link href="https://fonts.googleapis.com/css2?family=Pinyon+Script&family=Josefin+Sans:wght@400&display=swap" rel="stylesheet">
<style>
  :root {
    --paper: #ffffff;
    --flap-green: #d4fdc4;
    --flap-edge: #eefbea;
    --ink: #111111;
    --petal: #ef7f95;
    --petal-deep: #e05a72;
    --leaf: #9fd86a;
  }
  html, body {
    margin: 0;
    padding: 0;
    overflow: hidden;
    background: var(--paper);
  }
  .envelope {
    position: relative;
    width: 1043px;
    height: 1200px;
    overflow: hidden;
    background: var(--paper);
  }
  .envelope-dieline {
    position: absolute;
    inset: 0;
  }
  .return-address {
    position: absolute;
    left: 258px;
    top: 40px;
    width: 520px;
    text-align: center;
    transform: rotate(180deg);
    color: var(--ink);
  }
  .return-address .sender-name {
    font-family: "Pinyon Script", cursive;
    font-size: 34px;
    line-height: 1;
    margin: 0 0 24px;
  }
  .return-address .sender-line {
    font-family: "Josefin Sans", sans-serif;
    font-size: 14px;
    letter-spacing: 5px;
    text-transform: uppercase;
    margin: 0 0 26px;
    line-height: 1;
  }
  .recipient {
    position: absolute;
    right: 174px;
    top: 590px;
    text-align: right;
    color: var(--ink);
  }
  .recipient .recipient-name {
    font-family: "Pinyon Script", cursive;
    font-size: 42px;
    line-height: 1;
    margin: 0 0 34px;
  }
  .recipient .recipient-line {
    font-family: "Josefin Sans", sans-serif;
    font-size: 17px;
    letter-spacing: 4.6px;
    text-transform: uppercase;
    line-height: 1;
    margin: 0 -4px 26px 0;
  }
  .floral {
    position: absolute;
  }
  .floral-sprig {
    left: 131px;
    top: 284px;
    width: 78px;
    height: 66px;
  }
  .floral-bouquet {
    left: 131px;
    top: 478px;
    width: 210px;
    height: 330px;
  }
</style>
</head>
<body>
<main class="envelope">
  <svg class="envelope-dieline" width="1043" height="1200" viewBox="0 0 1043 1200" aria-hidden="true">
    <polygon class="top-flap" points="144,0 899,0 912,235 131,235" fill="var(--paper)" stroke="var(--flap-edge)" stroke-width="1"/>
    <polygon class="side-flap-left" points="0,263 131,235 131,808 0,780" fill="var(--flap-green)"/>
    <polygon class="side-flap-right" points="1043,263 912,235 912,808 1043,780" fill="var(--flap-green)"/>
    <rect class="front-panel" x="131" y="235" width="781" height="573" fill="var(--paper)"/>
    <polygon class="bottom-flap" points="131,808 912,808 899,1200 144,1200" fill="var(--flap-green)"/>
  </svg>

  <section class="return-address">
    <p class="sender-name">Daniel Carter</p>
    <p class="sender-line">1847 Willowbrook Lane, Oklahoma City,</p>
    <p class="sender-line">OK, Oklahoma, 73120</p>
  </section>

  <svg class="floral floral-sprig" viewBox="0 0 78 66" role="img" aria-label="Watercolour green leafy sprig">
    <defs>
      <linearGradient id="sprig-tone" x1="0" y1="0" x2="1" y2="1">
        <stop offset="0" stop-color="#b9e58e"/>
        <stop offset="1" stop-color="#e4f6d2"/>
      </linearGradient>
    </defs>
    <rect width="78" height="66" rx="20" fill="url(#sprig-tone)"/>
  </svg>

  <svg class="floral floral-bouquet" viewBox="0 0 210 330" role="img" aria-label="Watercolour bouquet of pink peonies with green leaves">
    <defs>
      <linearGradient id="bouquet-tone" x1="0" y1="0" x2="0" y2="1">
        <stop offset="0" stop-color="#dff3c9"/>
        <stop offset="0.4" stop-color="#c8e9a8"/>
        <stop offset="0.55" stop-color="#f3a7b5"/>
        <stop offset="1" stop-color="#e87590"/>
      </linearGradient>
    </defs>
    <rect width="210" height="330" rx="30" fill="url(#bouquet-tone)"/>
  </svg>

  <section class="recipient">
    <p class="recipient-name">Mr. and Mrs. Hartley</p>
    <p class="recipient-line">418 Maple Ridge Road</p>
    <p class="recipient-line">Portland, Oregon 97205</p>
  </section>
</main>
</body>
</html>
```